New Business Card Needed

I need a new business card for Willowmere Kitchen & Bath.
Logo is attached as well a my photo. Note: Make the logo Navy Blue.
Here is the text:
Desmond Ferrick
GC/Owner
Larkfield NC
704-555-0183
desmond@willowmereKB.example
www.willowmereKB.example
Tag line on card: DESIGN | QUALITY | CLEAR PLANS | FAIR PRICE
Trim size: 2.56" X 2.56"
This is where we aim to cut the cards.
Safe area: 2.4" X 2.4"
Make sure any important aspects of your design such as text and logos are inside of the safe area, otherwise they may be cut off.
Bleed area: 2.71 X 2.71
Make sure that your background extends to fill the bleed to avoid your Business Cards having white edges when trimmed.
On the back side. Use photo of kitchen attached.

```html
<!DOCTYPE html>
<html lang="en">
<head>
<meta charset="utf-8">
<title>Willowmere Kitchen &amp; Bath — Business Card</title>
<link href="https://fonts.googleapis.com/css2?family=Poppins:wght@400;500;600;700&display=swap" rel="stylesheet">
<style>
  :root{
    --stage:#1c1c1e;
    --ink:#111114;
    --navy:#161a2e;
    --paper:#ffffff;
    --muted:#3a3a3e;
    --photo-grey:#9a9a9c;
    --kitchen-dark:#2a2826;
    --kitchen-mid:#4a4540;
  }
  *{box-sizing:border-box;margin:0;padding:0}
  html,body{width:1200px;height:875px;overflow:hidden}
  body{
    background:var(--stage);
    font-family:"Poppins",sans-serif;
    position:relative;
  }
  .card{
    position:absolute;
    top:278px;
    width:540px;height:320px;
    border-radius:18px;
    overflow:hidden;
    box-shadow:0 14px 32px rgba(0,0,0,.5);
  }

  /* Back side */
  .card-back{left:40px}
  .kitchen-photo{
    position:absolute;inset:0;
    background:
      radial-gradient(ellipse at 30% 70%,rgba(110,100,90,.35),transparent 60%),
      linear-gradient(135deg,var(--kitchen-mid) 0%,var(--kitchen-dark) 55%,#1f1d1c 100%);
  }
  .kitchen-shade{position:absolute;inset:0;background:rgba(20,20,22,.5)}
  .back-brand{
    position:absolute;left:0;right:0;top:50%;transform:translateY(-50%);
    display:flex;align-items:center;justify-content:center;gap:14px;
    color:var(--paper);
  }
  .brand-square{width:18px;height:18px;background:currentColor;flex:none}
  .brand-name{
    font-weight:600;text-transform:uppercase;letter-spacing:.08em;line-height:1.15;
  }
  .back-brand .brand-name{font-size:26px}

  /* Front side */
  .card-front{left:620px;background:var(--paper)}
  .front-brand{
    position:absolute;left:34px;top:104px;
    display:flex;align-items:center;gap:10px;color:var(--navy);
  }
  .front-brand .brand-name{font-size:17px}
  .portrait{
    position:absolute;right:40px;top:24px;
    width:150px;height:150px;border-radius:50%;
    background:radial-gradient(circle at 50% 40%,#b4b4b6,var(--photo-grey) 70%);
  }
  .person{position:absolute;left:34px;top:168px;color:var(--navy)}
  .person-name{font-size:17px;font-weight:700;text-transform:uppercase;line-height:1.2}
  .person-role{font-size:10.5px;color:var(--muted);line-height:1.3}
  .contact{list-style:none;margin-top:6px}
  .contact li{display:flex;align-items:center;gap:7px;font-size:10.5px;color:var(--ink);line-height:1.55}
  .contact svg{width:10px;height:10px;flex:none}
  .location{
    position:absolute;left:300px;top:218px;
    display:flex;align-items:center;gap:7px;font-size:10.5px;color:var(--ink);
  }
  .location svg{width:10px;height:12px;fill:var(--ink)}
  .tagline-band{
    position:absolute;right:0;bottom:18px;left:250px;height:28px;
    background:var(--ink);color:var(--paper);
    display:flex;align-items:center;justify-content:center;
    font-size:10px;letter-spacing:.04em;text-transform:uppercase;
  }
  .side-notch{position:absolute;left:236px;bottom:18px;width:8px;height:28px;background:var(--ink)}
  .base-strip{position:absolute;left:0;right:0;bottom:0;height:12px;background:var(--ink)}
</style>
</head>
<body>

  <section class="card card-back" aria-label="Card back">
    <div class="kitchen-photo" role="img" aria-label="Photo of a finished kitchen with pendant lights and wooden cabinets"></div>
    <div class="kitchen-shade"></div>
    <div class="back-brand">
      <span class="brand-square"></span>
      <span class="brand-name">Willowmere<br>Kitchen &amp; Bath</span>
    </div>
  </section>

  <section class="card card-front" aria-label="Card front">
    <div class="front-brand">
      <span class="brand-square"></span>
      <span class="brand-name">Willowmere<br>Kitchen &amp; Bath</span>
    </div>

    <div class="portrait" role="img" aria-label="Portrait photo of Desmond Ferrick"></div>

    <div class="person">
      <p class="person-name">Desmond Ferrick</p>
      <p class="person-role">GC/Owner</p>
      <ul class="contact">
        <li><svg viewBox="0 0 24 24"><path fill="#111114" d="M6.6 10.8a15.1 15.1 0 0 0 6.6 6.6l2.2-2.2a1 1 0 0 1 1-.25 11.4 11.4 0 0 0 3.6.57 1 1 0 0 1 1 1V20a1 1 0 0 1-1 1A17 17 0 0 1 3 4a1 1 0 0 1 1-1h3.5a1 1 0 0 1 1 1c0 1.25.2 2.45.57 3.57a1 1 0 0 1-.25 1z"/></svg>704-555-0183</li>
        <li><svg viewBox="0 0 24 24"><path d="M2 5h20v14H2z M2 5l10 8 10-8" fill="none" stroke="#111114" stroke-width="2.4"/></svg>desmond@willowmereKB.example</li>
        <li><svg viewBox="0 0 24 24"><circle cx="12" cy="12" r="10" fill="none" stroke="#111114" stroke-width="2.4"/><path d="M2 12h20M12 2c3 3 3 17 0 20M12 2c-3 3-3 17 0 20" fill="none" stroke="#111114" stroke-width="2"/></svg>www.willowmereKB.example</li>
      </ul>
    </div>

    <div class="location">
      <svg viewBox="0 0 20 24"><path d="M10 0a8 8 0 0 0-8 8c0 6 8 16 8 16s8-10 8-16a8 8 0 0 0-8-8zm0 11a3 3 0 1 1 0-6 3 3 0 0 1 0 6z"/></svg>
      Larkfield NC
    </div>

    <div class="side-notch"></div>
    <div class="tagline-band">Design | Quality | Clear Plans | Fair Price</div>
    <div class="base-strip"></div>
  </section>

</body>
</html>
```